Tarolin Invitation Template (Editable Canva Design)

We are seeking a clean, professional invitation template for Tarolin that aligns with our company branding and colors. The most important requirement is that the design must be created in Canva so that our team can easily edit and reuse it for future events.
The invitation should include the following sections:
Event Blurb: A short paragraph describing the meeting, dinner, or event.
Date & Time: Clearly displayed and easy to read.
Location: With space for venue details.
Closing/Contact Section: A small closing note with instructions on who to reach out to, plus a closing blurb.
Design Requirements:
Must match Tarolin company colors
Utitlize both the TAROLIN & OMBRA FLEX QT logos (Tarolin is main and OMBRA FLEX QT is secondary)
Professional and polished, while still visually engaging.
Sized appropriately for both email and print sharing.
Delivered as a Canva template (so we can edit text, sections, and reuse easily).
I have attached an example of the template we used in the past that we do NOT like the look of - but you can get an idea of the different sections we need on the invite. Please do not try to make the new invites look anything like our old one.
Target Market(s)
Physicians (Pain Management)
Industry/Entity Type
Medical Device
Look and feel

```html
<!DOCTYPE html>
<html lang="en">
<head>
<meta charset="utf-8">
<title>Tarolin Invitation</title>
<link rel="stylesheet" href="https://fonts.googleapis.com/css2?family=Bebas+Neue&family=Poppins:ital,wght@0,400;0,500;0,600;0,700;1,400&display=swap">
<style>
  :root {
    --night: #111521;
    --panel: #030405;
    --green: #6db33f;
    --green-frame: #7db84c;
    --lime: #b6f02a;
    --white: #ffffff;
    --shadow-grey: #8a8a8a;
  }
  * { margin: 0; padding: 0; box-sizing: border-box; }
  html, body { width: 851px; height: 1200px; overflow: hidden; background: var(--night); }
  .invitation {
    position: relative; width: 851px; height: 1200px; overflow: hidden;
    background: var(--night);
    font-family: "Poppins", sans-serif; color: var(--white);
  }
  .particle-waves {
    position: absolute; inset: 0;
    background:
      radial-gradient(ellipse 260px 520px at 800px 180px, rgba(182,240,42,0.28), transparent 70%),
      radial-gradient(ellipse 300px 200px at 720px 1150px, rgba(120,220,60,0.30), transparent 70%),
      radial-gradient(ellipse 220px 260px at 60px 1080px, rgba(60,140,220,0.22), transparent 70%),
      radial-gradient(ellipse 200px 360px at 120px 600px, rgba(70,180,160,0.16), transparent 70%);
  }
  .dot-grid {
    position: absolute; top: 515px; height: 168px;
    background: linear-gradient(180deg, rgba(255,255,255,0.55), rgba(255,255,255,0.45));
    opacity: 0.55;
  }
  .dot-grid--left { left: 32px; width: 36px; }
  .dot-grid--right { left: 783px; width: 54px; }
  .frame {
    position: absolute; left: 86px; top: 86px; width: 678px; height: 1027px;
    background: var(--panel);
    border: 5px solid var(--green-frame); border-radius: 34px;
  }
  .brand {
    position: absolute; left: 0; width: 851px; top: 150px;
    text-align: center; color: var(--green);
    font-weight: 400; font-size: 74px; letter-spacing: 2px; line-height: 1;
  }
  .headline {
    position: absolute; left: 0; width: 851px; top: 290px;
    text-align: center;
    font-family: "Bebas Neue", sans-serif; font-size: 124px; line-height: 1;
    letter-spacing: 1px; color: var(--white);
    text-shadow: 4px 4px 0 var(--shadow-grey);
  }
  .info-box {
    position: absolute; left: 196px; width: 460px;
    background: var(--green);
    border: 2px solid var(--white); border-radius: 11px;
    display: flex; flex-direction: column; align-items: center; justify-content: center;
    text-align: center; color: var(--white);
  }
  .info-box--date { top: 440px; height: 83px; font-size: 31px; font-weight: 500; }
  .info-box--time { top: 549px; height: 83px; font-size: 31px; font-weight: 500; }
  .info-box--location { top: 658px; height: 107px; }
  .location-label { font-size: 21px; font-weight: 700; letter-spacing: 0.5px; margin-bottom: 8px; }
  .location-lines { font-size: 15.5px; font-weight: 500; line-height: 23px; }
  .blurb {
    position: absolute; left: 140px; width: 571px; top: 799px;
    text-align: center; font-style: italic; font-size: 21.5px; line-height: 27px;
  }
  .closing {
    position: absolute; left: 0; width: 851px; top: 943px;
    text-align: center; font-size: 13.5px; line-height: 20px;
  }
  .closing strong { font-weight: 700; }
  .contact-row {
    position: absolute; top: 1005px; left: 221px;
    display: flex; align-items: center; gap: 22px;
  }
  .contact-item { display: flex; align-items: center; gap: 9px; color: var(--green); font-weight: 600; font-size: 16.5px; }
  .contact-icon { width: 31px; height: 31px; }
  .partner-name {
    position: absolute; right: 130px; top: 1058px;
    font-size: 15px; font-weight: 600; letter-spacing: 0.5px; color: var(--white);
  }
</style>
</head>
<body>
<main class="invitation">
  <div class="particle-waves" role="img" aria-label="Flowing green and blue particle wave background"></div>
  <div class="dot-grid dot-grid--left" role="img" aria-label="White dot grid accent"></div>
  <div class="dot-grid dot-grid--right" role="img" aria-label="White dot grid accent"></div>

  <section class="frame"></section>

  <div class="brand">TAROLIN</div>
  <h1 class="headline">You’re Invited</h1>

  <div class="info-box info-box--date">TUESDAY- OCT, 29, 2025</div>
  <div class="info-box info-box--time">6:30 PM – 9:30 PM</div>
  <div class="info-box info-box--location">
    <div class="location-label">LOCATION</div>
    <div class="location-lines">THE GRAND BALLROOM, CITY CONFERENCE CENTER<br>123 BUSINESS AVENUE, SUITE 400</div>
  </div>

  <p class="blurb">Join us for an exclusive evening hosted by Tarolin, bringing together valued partners and colleagues for meaningful conversation, insights, and networking.</p>

  <p class="closing">We look forward to seeing you there!<br>For questions or special requests, please <strong>contact:</strong></p>

  <div class="contact-row">
    <div class="contact-item">
      <svg class="contact-icon" viewBox="0 0 32 32" aria-hidden="true">
        <circle cx="16" cy="16" r="16" fill="#6db33f"/>
        <g fill="none" stroke="#fff" stroke-width="1.5">
          <circle cx="16" cy="16" r="9"/>
          <ellipse cx="16" cy="16" rx="4" ry="9"/>
          <line x1="7" y1="16" x2="25" y2="16"/>
          <line x1="8.5" y1="11.5" x2="23.5" y2="11.5"/>
          <line x1="8.5" y1="20.5" x2="23.5" y2="20.5"/>
        </g>
      </svg>
      <span>events@tarolin.com</span>
    </div>
    <div class="contact-item">
      <svg class="contact-icon" viewBox="0 0 32 32" aria-hidden="true">
        <circle cx="16" cy="16" r="16" fill="#6db33f"/>
        <path d="M11 8.5c1-.6 1.8-.3 2.3.5l1.5 2.6c.4.8.2 1.5-.5 2l-1.2.8c.8 2 2.3 3.6 4.3 4.6l.9-1.1c.5-.7 1.3-.8 2-.4l2.6 1.6c.8.5 1 1.3.4 2.2l-1 1.4c-.7 1-2 1.3-3.2.9-4.6-1.6-8.2-5.3-9.6-10-.3-1.2 0-2.4 1-3.1z" fill="#fff"/>
      </svg>
      <span>555-010-2468</span>
    </div>
  </div>

  <div class="partner-name">OMBRA FLEX QT</div>
</main>
</body>
</html>
```